LPS AUDITION

I need a post card design (front only) with this on it:
Leap Pulse Stride (this is the main title to be in all caps)
Auditions
Date: Thursday June 30th
6:30-8:30 PM in person
Address: 4172 Kestrel BLVD, Oakland CA 94605
video submissions turn in by Sunday July 3rd, 2022 email:LeapPulseStride22@movenote.test
Teens and Adults welcomed

SO PLEASE COME UP WITH A DESIGN THATS COLORFUL AND INVITING THX!

```html
<!DOCTYPE html>
<html lang="en">
<head>
<meta charset="utf-8">
<title>Leap Pulse Stride – Auditions Postcard</title>
<link rel="stylesheet" href="https://fonts.googleapis.com/css2?family=Great+Vibes&family=Montserrat:wght@800&family=Nunito+Sans:ital,wght@0,400;0,700;1,400&display=swap">
<style>
  :root {
    --gold: #d6b66c;
    --ink: #0a0a0c;
    --paper: #ffffff;
    --stage: #e9e9e9;
    --leaf-dark: #1d2a1a;
    --leaf: #3c5a2c;
    --lawn: #4d6e34;
  }
  * { margin: 0; padding: 0; box-sizing: border-box; }
  html, body { width: 1200px; height: 869px; overflow: hidden; background: var(--stage); }
  .postcard {
    position: absolute; left: 0; top: 34px; width: 1200px; height: 801px;
    background: var(--ink); overflow: hidden;
    font-family: "Nunito Sans", sans-serif; color: var(--paper);
  }
  .dancer-photo {
    position: absolute; left: 420px; top: 0; width: 780px; height: 801px;
    background:
      linear-gradient(90deg, var(--ink) 0%, rgba(10,10,12,0.6) 30%, rgba(10,10,12,0) 60%),
      linear-gradient(180deg, var(--leaf-dark) 0%, var(--leaf) 45%, #2b2f2c 65%, var(--lawn) 85%);
  }
  .title {
    position: absolute; left: 60px; top: 40px;
    font-family: "Great Vibes", cursive; color: var(--gold);
    font-size: 118px; line-height: 92px; font-weight: 400;
  }
  .title span { display: block; }
  .title .l2 { padding-left: 70px; }
  .title .l3 { padding-left: 140px; }
  .badge {
    position: absolute; left: 68px; top: 411px;
    background: var(--gold); color: var(--ink);
    font-family: "Montserrat", sans-serif; font-weight: 800;
    font-size: 28px; line-height: 36px; padding: 0 8px; border-radius: 6px 6px 0 0;
  }
  .badge-rule { position: absolute; left: 68px; top: 447px; width: 477px; height: 2px; background: var(--gold); }
  .info { position: absolute; font-size: 33px; line-height: 40px; text-transform: uppercase; }
  .date { left: 110px; top: 468px; }
  .time { left: 354px; top: 468px; text-transform: none; }
  .time small { display: block; font-size: 28px; line-height: 30px; padding-left: 6px; }
  .icon { position: absolute; }
  .address { position: absolute; left: 108px; top: 563px; font-size: 26px; }
  .submit { position: absolute; left: 68px; top: 620px; font-size: 21px; line-height: 30px; }
  .submit b { font-weight: 700; }
  .submit .label { color: var(--gold); font-weight: 700; }
  .footer-wave { position: absolute; left: 0; top: 0; }
  .welcome {
    position: absolute; left: 144px; top: 757px;
    font-style: italic; font-size: 22px; color: var(--gold);
  }
</style>
</head>
<body>
<div class="postcard">
  <div class="dancer-photo" role="img" aria-label="Photo of a dancer in black leotard and skirt in an arabesque pose on a garden lawn"></div>

  <h1 class="title"><span class="l1">Leap</span><span class="l2">Pulse</span><span class="l3">Stride</span></h1>

  <div class="badge">AUDITIONS</div>
  <div class="badge-rule"></div>

  <svg class="icon" style="left:68px;top:476px" width="26" height="26" viewBox="0 0 26 26" fill="none" stroke="#d6b66c" stroke-width="2">
    <rect x="2" y="4" width="22" height="20" rx="3"/><line x1="2" y1="10" x2="24" y2="10"/>
    <line x1="8" y1="1" x2="8" y2="6"/><line x1="18" y1="1" x2="18" y2="6"/>
    <g fill="#d6b66c" stroke="none"><rect x="6" y="13" width="3" height="3"/><rect x="11.5" y="13" width="3" height="3"/><rect x="17" y="13" width="3" height="3"/><rect x="6" y="18" width="3" height="3"/><rect x="11.5" y="18" width="3" height="3"/><rect x="17" y="18" width="3" height="3"/></g>
  </svg>
  <p class="info date">Thursday<br>June 30th</p>

  <svg class="icon" style="left:320px;top:477px" width="26" height="26" viewBox="0 0 26 26" fill="none" stroke="#d6b66c" stroke-width="2.4">
    <circle cx="13" cy="13" r="11"/><polyline points="13,6 13,14 10,18"/>
  </svg>
  <p class="info time">6:30-8:30 PM<small>in person</small></p>

  <svg class="icon" style="left:72px;top:565px" width="22" height="30" viewBox="0 0 22 30">
    <path d="M11 0C5 0 0 5 0 11c0 8 11 19 11 19s11-11 11-19C22 5 17 0 11 0z" fill="#d6b66c"/>
    <circle cx="11" cy="11" r="4" fill="#0a0a0c"/>
  </svg>
  <p class="address">4172 Kestrel BLVD, Oakland CA 94605</p>

  <p class="submit">Video submissions turn in by <b>Sunday July 3rd, 2022</b><br><span class="label">Email:</span> LeapPulseStride22@movenote.test</p>

  <svg class="footer-wave" width="1200" height="801" viewBox="0 0 1200 801">
    <path d="M0 762 C140 720 300 720 520 736 C760 752 960 800 1100 790 C1160 784 1185 770 1200 760 L1200 801 L0 801 Z" fill="#ffffff"/>
    <path d="M0 740 C80 712 180 700 240 720 C160 716 80 728 0 756 Z" fill="#d6b66c"/>
    <path d="M800 795 C980 800 1140 760 1200 665 L1200 700 C1150 770 1000 800 800 795 Z" fill="#d6b66c"/>
  </svg>
  <p class="welcome">Teens and Adults welcomed</p>
</div>
</body>
</html>
```